50's-style gig poster for a birthday bash

My wife was born in 1957 and is turning 57 next month. I'm throwing a surprise party for her, and thought it would be fun to have a 18x24 poster printed and framed for the event. Attached is a poster from a Rufus Kettle gig in 1957. I'd like something like this, with a tinted B&W head shot of my wife, with similar fonts and background color schemes. The copy will be HELGA at the top (where the name RUFUS appears), with 57X57 under it, and the word Celebration where the word Quartet currently appears. The rest of the copy will be provided to you. Thanks for your interest and I look forward to working with you.

```html
<!DOCTYPE html>
<html lang="en">
<head>
<meta charset="utf-8">
<title>HELGA 57X57 Celebration</title>
<link rel="stylesheet" href="https://fonts.googleapis.com/css2?family=Anton&family=Fraunces:opsz,wght@144,900&family=Open+Sans:ital,wght@0,800;1,800&family=Playfair+Display:ital,wght@1,900&display=swap">
<style>
  :root {
    --cream: #fcefd9;
    --ticket: #fcf0d6;
    --navy: #1d1866;
    --red: #ff2a00;
    --white: #ffffff;
    --gold: #ffd84a;
    --butter: #fff5b3;
    --ink: #1a1545;
    --shadow: rgba(0, 0, 0, 0.6);
  }
  * { margin: 0; padding: 0; box-sizing: border-box; }
  html, body { width: 853px; height: 1200px; overflow: hidden; background: var(--cream); }
  .poster { position: relative; width: 853px; height: 1200px; background: var(--cream); overflow: hidden; }

  .stripe { position: absolute; top: 30px; height: 1138px; }
  .stripe--navy { background: var(--navy); }
  .stripe--red { background: var(--red); }

  .the-label {
    position: absolute; left: 66px; top: 54px;
    font: italic 800 21px/1 "Open Sans", sans-serif; color: var(--white);
    letter-spacing: 1px;
  }

  .headline { position: absolute; left: 0; top: 0; width: 853px; height: 560px; overflow: visible; }
  .headline text {
    font-family: "Anton", sans-serif; fill: var(--white); text-anchor: middle;
    filter: drop-shadow(7px 7px 5px rgba(0,0,0,.6));
  }
  .headline-letter { font-size: 198px; }
  .headline-digit { font-size: 280px; }

  .portrait {
    position: absolute; left: 62px; top: 548px; width: 272px; height: 328px;
    background: linear-gradient(160deg, #c9ccd6 0%, #8d93a6 45%, #4c5266 100%);
    border: 6px solid #f4f4f6;
    transform: rotate(-5deg);
    box-shadow: 6px 8px 10px var(--shadow);
  }

  .celebration { position: absolute; left: 420px; top: 548px; width: 360px; height: 100px; overflow: visible; }
  .celebration text {
    font-family: "Fraunces", serif; font-weight: 900; font-size: 60px;
    fill: var(--butter); stroke: var(--ink); stroke-width: 2.5px; paint-order: stroke;
    filter: drop-shadow(4px 4px 3px rgba(0,0,0,.6));
  }

  .lineup { position: absolute; left: 350px; top: 646px; width: 452px; text-align: center; color: var(--white); font-family: "Open Sans", sans-serif; }
  .lineup-label { font: italic 800 18px/1.2 "Open Sans", sans-serif; color: var(--gold); }
  .lineup-names { font-weight: 800; font-size: 18px; line-height: 26px; }

  .date-badge {
    position: absolute; left: 450px; top: 768px; width: 266px; height: 160px;
    border-radius: 50%; background: var(--ticket);
    box-shadow: 4px 6px 8px var(--shadow);
    display: flex; flex-direction: column; justify-content: center; align-items: center;
    font: italic 800 27px/36px "Open Sans", sans-serif; color: var(--navy); text-align: center;
  }

  .also-label {
    position: absolute; left: 136px; top: 896px;
    font: italic 800 20px/1 "Open Sans", sans-serif; color: var(--white);
    text-shadow: 2px 2px 3px var(--shadow);
  }
  .support-act {
    position: absolute; left: 0; top: 942px; width: 853px; text-align: center;
    font: italic 900 60px/1 "Playfair Display", serif; color: var(--white);
    text-shadow: 5px 5px 6px var(--shadow);
  }

  .venue {
    position: absolute; left: 65px; top: 1023px; width: 718px; height: 105px;
    background: var(--ticket); box-shadow: 6px 6px 8px var(--shadow);
    display: flex; flex-direction: column; justify-content: center; align-items: center;
    font-family: "Playfair Display", serif; font-style: italic; font-weight: 900; color: var(--navy);
  }
  .venue-name { font-size: 27px; line-height: 36px; letter-spacing: 1px; }
  .venue-address { font-size: 29px; line-height: 38px; }
</style>
</head>
<body>
<main class="poster">
  <div class="stripe stripe--navy" style="left:32px;width:156px"></div>
  <div class="stripe stripe--red" style="left:193px;width:157px"></div>
  <div class="stripe stripe--navy" style="left:354px;width:156px"></div>
  <div class="stripe stripe--red" style="left:515px;width:157px"></div>
  <div class="stripe stripe--navy" style="left:676px;width:145px"></div>

  <div class="the-label">THE</div>

  <h1>
    <svg class="headline" viewBox="0 0 853 560" role="img" aria-label="HELGA 57X57">
      <text class="headline-letter" x="110" y="275">H</text>
      <text class="headline-letter" x="271" y="275">E</text>
      <text class="headline-letter" x="432" y="275">L</text>
      <text class="headline-letter" x="593" y="275">G</text>
      <text class="headline-letter" x="748" y="275">A</text>
      <text class="headline-digit" x="110" y="540">5</text>
      <text class="headline-digit" x="271" y="540">7</text>
      <text class="headline-digit" x="432" y="540">X</text>
      <text class="headline-digit" x="593" y="540">5</text>
      <text class="headline-digit" x="748" y="540">7</text>
    </svg>
  </h1>

  <div class="portrait" role="img" aria-label="Tinted black and white head shot of Helga, smiling"></div>

  <svg class="celebration" viewBox="0 0 360 100" aria-label="Celebration">
    <defs><path id="celebration-arc" d="M10 86 Q180 50 350 70"/></defs>
    <text><textPath href="#celebration-arc" startOffset="50%" text-anchor="middle">Celebration</textPath></text>
  </svg>

  <div class="lineup">
    <div class="lineup-label">Featuring:</div>
    <div class="lineup-names">
      The Marlowes &nbsp;•&nbsp; The Fenwicks<br>
      The Beaumonts &nbsp;•&nbsp; The Ashby-Carrows<br>
      The Pembertons &nbsp;•&nbsp; The Whitfords
    </div>
  </div>

  <div class="date-badge">
    <span>One</span>
    <span>Night Only</span>
    <span>April 4, 2014</span>
    <span>6 PM</span>
  </div>

  <div class="also-label">Also Appearing</div>
  <div class="support-act">The Chirps &amp; Lou Brandt</div>

  <div class="venue">
    <div class="venue-name">BISTRO MARCEL</div>
    <div class="venue-address">1414 Cedar Lane, Oakvale, California</div>
  </div>
</main>
</body>
</html>
```